Telmora Coaching flyer (women local)

Strapline: Do you want a more fulfilling and meaningful life?
Make 2015 a year for positive change

Image of an attractive woman in contemplation:

• I’ve lost my identity and wondering what life is about.

• I want more intimacy in my relationship

• I hate my career and don’t know what’s right for me

Personal Development Coaching can help you:

Testimonials from our clients:

‘I have changed the way I approach my daily life in order to achieve more for myself’.

‘Coaching has helped me change the way I think, focusing more on positive rather than negative thoughts’.

‘Without coaching, I believe that my life would have remained stagnant’.

‘ I have made the leap to set up my own business and have increased my income three fold’.

‘Coaching has helped me to grow closer than ever to my husband’.

Any relevant image and image of myself (included)

Why Telmora?

• Certified Personal Development Coach

• Experience coaching individuals wanting to effect change

Nadia is a specialist in coaching for:

• Building confidence

• Feeling motivated and getting out of a rut

• Enhancing relationships with partners or family

• Making changes in your career or business

Book your free consultation (this should stand out)

e: nadia@telmora-example.co.uk t: 0798 512 6043 w: www.telmora-example.co.uk (include logo, but change ‘Telmora Consulting’ to ‘Telmora Coaching’)
f: www.facebook.com/telmora-example.co.uk t: @ndtelmora

* Notes in brackets are only instructions and not to be included as part of the flyer.

Flyer is is A5

Please not this flyer can be double sided as I feel there will be too much text for one side. Could you use image of woman in contemplation on front but not too depressing.

```html
<!DOCTYPE html>
<html lang="en">
<head>
<meta charset="utf-8">
<title>Telmora Coaching – Flyer Front</title>
<link rel="stylesheet" href="https://fonts.googleapis.com/css2?family=Kreon:wght@300;400&family=Noticia+Text:ital@1&display=swap">
<style>
  :root {
    --navy: #1f3163;
    --purple: #7c3f98;
    --cyan: #16b3dd;
    --quote: #7a3a8e;
    --paper: #ffffff;
    --stage: #ebeaee;
  }
  html, body {
    margin: 0;
    padding: 0;
    width: 1040px;
    height: 1200px;
    overflow: hidden;
    background: var(--stage);
  }
  .flyer {
    position: absolute;
    left: 121px;
    top: 37px;
    width: 614px;
    height: 865px;
    background: linear-gradient(180deg, var(--paper) 60%, #f3f2f5 100%);
    transform: scale(1.3);
    transform-origin: top left;
    overflow: hidden;
    font-family: "Kreon", Georgia, serif;
  }
  .hero-photo {
    position: absolute;
    left: 0; top: 0;
    width: 614px; height: 405px;
    background:
      radial-gradient(ellipse 160px 190px at 200px 190px, #b89382 0%, #8a6a5c 45%, transparent 75%),
      linear-gradient(100deg, #d9d3cc 0%, #cfc8c0 40%, #ddd8d2 70%, #c8c0b8 100%);
  }
  .hero-rule {
    position: absolute;
    left: 0; top: 405px;
    width: 614px; height: 6px;
    background: var(--cyan);
  }
  .bubbles {
    position: absolute;
    left: 0; top: 0;
    width: 614px; height: 520px;
  }
  .bubble-text {
    position: absolute;
    width: 150px;
    text-align: center;
    font-size: 20.5px;
    line-height: 22px;
    font-weight: 400;
    margin: 0;
  }
  .bubble-text--identity { left: 416px; top: 45px; color: #3fc3ea; }
  .bubble-text--intimacy { left: 423px; top: 218px; color: #ffffff; transform: rotate(-5deg); }
  .bubble-text--career { left: 425px; top: 367px; color: var(--navy); }

  .headline {
    position: absolute;
    left: 33px; top: 432px;
    margin: 0;
    font-size: 39px;
    line-height: 44px;
    font-weight: 400;
    color: var(--cyan);
  }
  .subhead {
    position: absolute;
    left: 345px; top: 502px;
    margin: 0;
    font-size: 27px;
    line-height: 29px;
    font-weight: 400;
    color: var(--navy);
  }
  .section-title {
    position: absolute;
    left: 38px; top: 600px;
    margin: 0;
    font-size: 27px;
    font-weight: 400;
    color: var(--navy);
  }
  .section-rule {
    position: absolute;
    left: 38px; top: 636px;
    width: 528px; height: 14px;
  }
  .testimonials-label {
    position: absolute;
    left: 39px; top: 670px;
    margin: 0;
    font-size: 14px;
    font-weight: 400;
    letter-spacing: 0.2px;
    text-transform: uppercase;
    color: var(--cyan);
  }
  .testimonial {
    position: absolute;
    margin: 0;
    width: 240px;
    font-family: "Noticia Text", Georgia, serif;
    font-style: italic;
    font-size: 14px;
    line-height: 17.5px;
    color: var(--quote);
  }
  .t1 { left: 40px; top: 698px; }
  .t2 { left: 40px; top: 774px; }
  .t3 { left: 351px; top: 666px; width: 230px; }
  .t4 { left: 351px; top: 737px; width: 230px; }
  .t5 { left: 351px; top: 805px; width: 230px; }
</style>
</head>
<body>
  <main class="flyer">
    <div class="hero-photo" role="img" aria-label="Photograph of a woman leaning against a pale wall, looking thoughtfully into the distance"></div>
    <div class="hero-rule"></div>

    <svg class="bubbles" viewBox="0 0 614 520" aria-hidden="true">
      <g class="bubble bubble--navy" fill="#1f3163">
        <circle cx="491" cy="100" r="84"/>
        <path d="M520 170 L552 190 L548 150 Z"/>
      </g>
      <g class="bubble bubble--purple" fill="#7c3f98">
        <circle cx="499" cy="258" r="84"/>
        <path d="M445 300 L442 350 L480 330 Z"/>
      </g>
      <g class="bubble bubble--cyan" fill="#16b3dd">
        <circle cx="500" cy="423" r="84"/>
        <path d="M520 350 L560 326 L558 380 Z"/>
      </g>
    </svg>

    <p class="bubble-text bubble-text--identity">I’ve lost my identity and wondering what life is about.</p>
    <p class="bubble-text bubble-text--intimacy">I want more intimacy in my relationship.</p>
    <p class="bubble-text bubble-text--career">I hate my career and don’t know what’s right for me.</p>

    <h1 class="headline">Do you want a more<br>fulfilling and<br>meaningful life?</h1>
    <p class="subhead">Make 2015 a year<br>for positive change</p>

    <h2 class="section-title">Personal Development Coaching can help you:</h2>
    <svg class="section-rule" viewBox="0 0 528 14" aria-hidden="true">
      <line x1="0" y1="1" x2="528" y2="1" stroke="#16b3dd" stroke-width="1.5"/>
      <path d="M10 1 L30 1 L20 13 Z" fill="#16b3dd"/>
    </svg>

    <h3 class="testimonials-label">Testimonials from our clients:</h3>
    <p class="testimonial t1">‘I have changed the way I approach my daily life in order to achieve more for myself’.</p>
    <p class="testimonial t2">‘Coaching has helped me change the way I think, focusing more on positive rather than negative thoughts’.</p>
    <p class="testimonial t3">‘Without coaching, I believe that my life would have remained stagnant’.</p>
    <p class="testimonial t4">‘ I have made the leap to set up my own business and have increased my income three fold’.</p>
    <p class="testimonial t5">‘Coaching has helped me to grow closer than ever to my husband’.</p>
  </main>
</body>
</html>
```